Business Card Design

I'd like to have some business cards designed using my new logo. I am an accountant and company secretary and offer these services through Halvorsen Global Advisory Pty Ltd. I am the sole Director of the company. Please let me know if you require any further logo files.

Industry/Entity Type

Business

```html
<!DOCTYPE html>
<html lang="en">
<head>
<meta charset="utf-8">
<title>Halvorsen Global Advisory – Business Card</title>
<link rel="stylesheet" href="https://fonts.googleapis.com/css2?family=Cormorant+Garamond:wght@500;600&family=Open+Sans:wght@400;600;700&display=swap">
<style>
  :root {
    --page-bg: #6f7a88;
    --card-white: #ffffff;
    --card-white-shade: #eeeeee;
    --card-grey-light: #9a9a9a;
    --card-grey-dark: #6a6a6a;
    --band-grey: #6c6c6c;
    --brand-blue: #1f5fd0;
    --text-grey: #5c5c5c;
    --text-dark: #4a4a4a;
    --on-dark: #ffffff;
  }
  * { box-sizing: border-box; margin: 0; padding: 0; }
  html, body { width: 1200px; height: 1024px; overflow: hidden; }
  body {
    background: var(--page-bg);
    font-family: "Open Sans", sans-serif;
    position: relative;
  }
  .card {
    position: absolute;
    left: 190px;
    width: 820px;
    height: 469px;
    border-radius: 28px;
    overflow: hidden;
    box-shadow: 0 10px 30px rgba(0,0,0,0.25);
  }
  /* ---------- back ---------- */
  .card-back {
    top: 30px;
    background: radial-gradient(ellipse at 60% 20%, var(--card-grey-light), var(--card-grey-dark) 80%);
    color: var(--on-dark);
  }
  .back-lockup {
    position: absolute;
    left: 200px;
    top: 160px;
    display: flex;
    align-items: center;
    gap: 22px;
  }
  .wordmark {
    font-family: "Open Sans", sans-serif;
    font-weight: 700;
    font-size: 64px;
    letter-spacing: 2px;
    line-height: 1;
  }
  .back-lockup .wordmark { color: var(--on-dark); }
  .divider {
    width: 2px;
    height: 110px;
    background: currentColor;
  }
  .company-name {
    font-family: "Cormorant Garamond", serif;
    font-weight: 600;
    text-transform: uppercase;
    font-size: 27px;
    line-height: 1.02;
    letter-spacing: 1px;
  }
  .back-web {
    position: absolute;
    left: 430px;
    top: 320px;
    font-size: 19px;
    letter-spacing: 0.5px;
  }
  /* ---------- front ---------- */
  .card-front {
    top: 525px;
    background: radial-gradient(ellipse at 70% 30%, var(--card-white), var(--card-white-shade) 90%);
  }
  .front-lockup {
    position: absolute;
    left: 60px;
    top: 60px;
    display: flex;
    flex-direction: column;
    gap: 14px;
    color: var(--text-grey);
  }
  .front-lockup .wordmark { color: var(--brand-blue); font-size: 52px; }
  .front-name-row { display: flex; align-items: center; gap: 14px; }
  .front-name-row .divider { height: 90px; width: 1.5px; }
  .front-name-row .company-name { font-size: 23px; font-weight: 500; }
  .contact {
    position: absolute;
    left: 470px;
    top: 150px;
    color: var(--text-grey);
  }
  .person-name {
    font-weight: 700;
    font-size: 24px;
    color: var(--text-dark);
  }
  .person-role {
    font-size: 17px;
    color: var(--brand-blue);
    margin-bottom: 14px;
  }
  .contact-list { list-style: none; font-size: 17px; line-height: 1.45; }
  .contact-list li { display: flex; align-items: center; gap: 10px; }
  .contact-list svg { width: 14px; height: 14px; fill: var(--brand-blue); flex: none; }
  .registry { margin-top: 8px; font-size: 17px; line-height: 1.35; }
  .edge-band {
    position: absolute;
    left: 0; right: 0; bottom: 0;
    height: 26px;
    display: flex;
  }
  .edge-band .band-grey { flex: 1; background: var(--band-grey); }
  .edge-band .band-blue { width: 170px; background: var(--brand-blue); }
</style>
</head>
<body>
  <section class="card card-back" aria-label="Card back">
    <div class="back-lockup">
      <span class="wordmark">HGA</span>
      <span class="divider"></span>
      <p class="company-name">Halvorsen<br>Global Advisory<br>Pty Ltd</p>
    </div>
    <p class="back-web">www.HGA.com.au</p>
  </section>

  <section class="card card-front" aria-label="Card front">
    <div class="front-lockup">
      <span class="wordmark">HGA</span>
      <div class="front-name-row">
        <span class="divider"></span>
        <p class="company-name">Halvorsen<br>Global Advisory<br>Pty Ltd</p>
      </div>
    </div>

    <div class="contact">
      <p class="person-name">Mark Ellison</p>
      <p class="person-role">Director</p>
      <ul class="contact-list">
        <li><svg viewBox="0 0 16 16" aria-hidden="true"><path d="M3 1l3 3-1.5 2c1 2 3 4 5 5L11.5 9.5l3 3-2 2.5C6 14 2 10 1 3z"/></svg>0412558019</li>
        <li><svg viewBox="0 0 16 16" aria-hidden="true"><path d="M4 1h8v14H4zM5.5 2.5v9h5v-9z"/></svg>0412558019</li>
        <li><svg viewBox="0 0 16 16" aria-hidden="true"><path d="M1 3h14v10H1zM2 4l6 5 6-5z"/></svg>info@HGA.com.au</li>
        <li><svg viewBox="0 0 16 16" aria-hidden="true"><circle cx="8" cy="8" r="7"/></svg>www.HGA.com.au</li>
      </ul>
      <p class="registry">Eastbank 6208<br>ABN: 51 204 773 618<br>ACN: 204 773 618</p>
    </div>

    <div class="edge-band">
      <span class="band-grey"></span>
      <span class="band-blue"></span>
    </div>
  </section>
</body>
</html>
```